Willow Brook Meadows - Pelham Ridge Loop

Please use this range of Flyers. Info can be found on our Facebook Page Willow Brook Meadows. W

Colour range- Black with Orange Trim. Logo attached.

Target Market(s)

Horse Owners

Colors
ffcf3e
f78f20
f37122

Requirements
Must have
• Our Logo. Tri-fold
Should not have
• Other photos other than supplied. Do not mix Willow Brook Meadows with Willow Brook Equine Sanctuary. This is only for Willow Brook Meadows.

```html
<!DOCTYPE html>
<html lang="en">
<head>
<meta charset="utf-8">
<title>Willow Brook Meadows – Pelham Ridge Loop Flyer</title>
<link rel="stylesheet" href="https://fonts.googleapis.com/css2?family=Montserrat:wght@400;600;700;800;900&display=swap">
<style>
  :root{
    --ink:#141414;
    --ink-soft:#2a2a2a;
    --orange:#f37122;
    --orange-mid:#f78f20;
    --gold:#ffcf3e;
    --paper:#ffffff;
    --stage:#e9e6e2;
    --muted:#555555;
  }
  *{box-sizing:border-box;margin:0;padding:0}
  html,body{width:1200px;height:674px;overflow:hidden}
  body{background:var(--stage);font-family:"Montserrat",sans-serif;position:relative}

  .flyer{position:absolute;left:380px;top:24px;width:440px;height:626px;background:var(--paper);overflow:hidden;box-shadow:0 10px 30px rgba(0,0,0,.18)}
  .flyer svg.shapes{position:absolute;inset:0;width:100%;height:100%}

  .photo{position:absolute}
  .photo--hero{left:0;top:0;width:440px;height:285px;background:linear-gradient(120deg,#7a4a24 0%,#b9773c 35%,#d39a5e 55%,#8d6a45 80%,#5a4630 100%)}
  .photo--paddock{left:262px;top:328px;width:170px;height:108px;background:linear-gradient(160deg,#dfe3d6 0%,#b8c39b 45%,#6f8a4a 75%,#4e6536 100%)}
  .photo--rider{left:0;top:444px;width:230px;height:130px;background:linear-gradient(170deg,#cfd7c4 0%,#93a877 40%,#5f7a3d 70%,#44582b 100%)}

  .brand{position:absolute;left:18px;top:14px;display:flex;align-items:center;gap:8px;color:var(--paper);font-weight:800;font-size:15px;letter-spacing:.02em;line-height:1.05;text-transform:uppercase;width:170px}
  .brand__mark{width:12px;height:12px;background:var(--orange);flex:none}

  .hero-title{position:absolute;left:22px;top:96px;font-weight:900;font-size:60px;line-height:.92;letter-spacing:.01em}
  .hero-title .line-dark{color:var(--ink);display:block}
  .hero-title .line-light{color:var(--paper);display:block}
  .hero-sub{position:absolute;left:22px;top:218px;background:var(--ink);color:var(--orange-mid);font-size:8px;font-weight:700;letter-spacing:.06em;padding:3px 8px}

  .band-title{position:absolute;left:20px;top:290px;color:var(--paper);font-weight:800;font-size:17px;letter-spacing:.02em}

  .intro{position:absolute;left:20px;top:328px;width:230px}
  .intro__title{font-weight:900;font-size:19px;color:var(--ink);letter-spacing:.01em}
  .intro__sub{font-size:7px;font-weight:700;color:var(--orange);letter-spacing:.05em;margin:2px 0 6px}
  .intro__text{font-size:8.5px;line-height:1.45;color:var(--muted)}

  .features{position:absolute;left:248px;top:458px;list-style:none}
  .features li{color:var(--paper);font-weight:700;font-size:11px;line-height:19.5px;display:flex;align-items:center;gap:8px}
  .features li::before{content:"";width:6px;height:6px;border-radius:50%;background:var(--orange)}

  .footer-links{position:absolute;left:92px;top:590px;width:340px;display:flex;justify-content:space-around;font-weight:800;font-size:10px;color:var(--ink);letter-spacing:.03em}
  .phone-icon{position:absolute;left:20px;top:583px;width:30px;height:30px}
</style>
</head>
<body>
  <main class="flyer" aria-label="Willow Brook Meadows – Pelham Ridge Loop flyer">
    <div class="photo photo--hero" role="img" aria-label="Photo of a rider leading a pale horse on a sunny trail"></div>
    <div class="photo photo--paddock" role="img" aria-label="Photo of a person with a horse in a green paddock"></div>
    <div class="photo photo--rider" role="img" aria-label="Photo of a rider on a dark horse in a field"></div>

    <svg class="shapes" viewBox="0 0 440 626" aria-hidden="true">
      <!-- header: dark logo plate and orange trim -->
      <polygon points="0,0 210,0 185,58 0,58" fill="var(--ink)"/>
      <polygon points="220,0 440,0 440,40 204,40" fill="var(--orange)"/>
      <polygon points="300,40 440,40 440,52 295,52" fill="var(--ink)"/>
      <!-- hero warm overlay on the left for the headline -->
      <polygon points="0,58 250,58 200,285 0,285" fill="var(--orange)" opacity=".45"/>
      <!-- black title band -->
      <polygon points="0,285 330,285 312,318 0,318" fill="var(--ink)"/>
      <polygon points="330,285 440,285 440,292 327,292" fill="var(--orange)"/>
      <!-- paddock photo frame -->
      <polygon points="262,328 290,328 262,380" fill="var(--ink)"/>
      <polygon points="432,384 432,436 404,436" fill="var(--ink)"/>
      <!-- feature list panel -->
      <polygon points="230,444 440,444 440,574 230,574" fill="var(--ink)"/>
      <polygon points="200,444 230,444 230,574 200,574" fill="var(--ink)" opacity="0"/>
      <!-- footer -->
      <rect x="0" y="574" width="440" height="52" fill="var(--ink)"/>
      <polygon points="82,580 440,580 440,620 70,620" fill="var(--orange)"/>
    </svg>

    <div class="brand"><span class="brand__mark"></span>Willow Brook Meadows</div>

    <h1 class="hero-title"><span class="line-dark">LOREM</span><span class="line-light">IPSUM</span></h1>
    <p class="hero-sub">LOREM IPSUM DOLOR SIT AMET CONSECTETUR</p>

    <h2 class="band-title">LOREM IPSUM</h2>

    <section class="intro">
      <h3 class="intro__title">LOREM IPSUM</h3>
      <p class="intro__sub">DOLOR SIT AMET CONSECTETUR ADIPISCING</p>
      <p class="intro__text">Lorem Ipsum is simply dummy text of the printing and typesetting industry. Lorem scrambled it to make a type specimen book. It has survived not only five centuries but also.</p>
    </section>

    <ul class="features">
      <li>Lorem Ipsum</li>
      <li>Lorem Ipsum</li>
      <li>Lorem Ipsum</li>
      <li>Lorem Ipsum</li>
      <li>Lorem Ipsum</li>
    </ul>

    <svg class="phone-icon" viewBox="0 0 30 30" aria-hidden="true">
      <circle cx="15" cy="15" r="13.5" fill="none" stroke="var(--paper)" stroke-width="2"/>
      <path d="M10.5 8.5c.6-.6 1.5-.5 2 .1l1.3 1.7c.4.5.4 1.2-.1 1.7l-.9.9c.8 1.7 2.1 3 3.8 3.8l.9-.9c.5-.5 1.2-.5 1.7-.1l1.7 1.3c.6.5.7 1.4.1 2l-.9.9c-.9.9-2.3 1.1-3.5.5-3-1.5-5.4-3.9-6.9-6.9-.6-1.2-.4-2.6.5-3.5z" fill="var(--paper)"/>
    </svg>
    <div class="footer-links">
      <span>LOREM IPSUM</span><span>LOREM IPSUM</span><span>LOREM IPSUM</span>
    </div>
  </main>
</body>
</html>
```